Label Design for honey from a small farm in Italy

We need a label for our Acacia's honey .
We are a little farm in Italy and we would like something like organic, raw and simple.
Maybe with botanical drawing with different color like watercolor o something like that (very important natural and easy)
the jar for 1kg of honey: Capacity: 780 ml - Height: 137 mm - Diameter: ∅ 94 mm
- size approx h 5,5 x 10/14cm ( we use the same label for kg and 500 gr jar)

Industry/Entity Type

Farm

Requirements
Must have
• the writings:
- Acacia
- Miele italiano di Acacia
- Da consumarsi preferibilmente entro: ( and below the space to put the date by the hands)
- some space to put some presentation of the farm or some phrases
- our logo
- the space to put the weight by the hands
- Prodotto da Azienda Agricola ...(produced by Farm Name and address....)
- Confezionato presso Apicoltura... (packaged at apiculture Name and address..)
- graphic of Acacia’s flowers ( like drawing)
Should not have
• Barcode
nutritional table

```html
<!DOCTYPE html>
<html lang="it">
<head>
<meta charset="utf-8">
<title>Etichetta Miele di Acacia</title>
<link rel="stylesheet" href="https://fonts.googleapis.com/css2?family=Archivo+Black&family=Marcellus&family=Nunito+Sans:wght@400;600&display=swap">
<style>
  :root {
    --frame: #978a5b;
    --gold: #cc9a2e;
    --gold-light: #e3c78e;
    --plum: #76174b;
    --plum-soft: #9a5a7a;
    --mint: #b5e3d3;
    --cream: #f3eca0;
    --ink: #141414;
    --note: #b9b9b9;
    --page: #ffffff;
  }
  html, body {
    margin: 0;
    padding: 0;
    width: 1200px;
    height: 664px;
    overflow: hidden;
    background: var(--page);
  }
  .canvas {
    position: relative;
    width: 1200px;
    height: 664px;
  }
  .label {
    position: absolute;
    left: 91px;
    top: 79px;
    width: 1030px;
    height: 472px;
    background: var(--frame);
  }
  .label__field {
    position: absolute;
    left: 15px;
    top: 13px;
    width: 1003px;
    height: 446px;
    background: var(--gold);
  }
  .botanical {
    position: absolute;
    left: 15px;
    top: 13px;
    width: 448px;
    height: 446px;
    background:
      radial-gradient(circle at 18% 22%, rgba(246, 222, 60, .55) 0 9%, transparent 16%),
      radial-gradient(circle at 72% 12%, rgba(246, 222, 60, .5) 0 8%, transparent 15%),
      radial-gradient(circle at 85% 58%, rgba(246, 222, 60, .5) 0 9%, transparent 16%),
      radial-gradient(circle at 12% 70%, rgba(246, 222, 60, .5) 0 8%, transparent 15%),
      radial-gradient(circle at 55% 92%, rgba(246, 222, 60, .5) 0 9%, transparent 16%),
      radial-gradient(circle at 40% 45%, rgba(110, 190, 160, .35) 0 20%, transparent 40%),
      linear-gradient(135deg, #e6f3ea, #f7f6df 50%, #dfeee3);
  }
  .art {
    position: absolute;
    left: 0;
    top: 0;
    width: 1200px;
    height: 664px;
  }
  .brand {
    position: absolute;
    left: 220px;
    top: 222px;
    width: 200px;
    display: flex;
    align-items: center;
    justify-content: center;
    gap: 8px;
    font-family: "Nunito Sans", sans-serif;
    font-weight: 600;
    font-size: 22px;
    letter-spacing: 1px;
    color: var(--mint);
    white-space: nowrap;
  }
  .brand__dot {
    width: 10px;
    height: 10px;
    border-radius: 50%;
    background: var(--mint);
  }
  .variety {
    position: absolute;
    left: 180px;
    top: 298px;
    width: 300px;
    text-align: center;
    font-family: "Archivo Black", sans-serif;
    font-size: 58px;
    line-height: 1;
    color: #fff;
  }
  .subtitle {
    position: absolute;
    left: 180px;
    top: 382px;
    width: 300px;
    text-align: center;
    font-family: "Marcellus", serif;
    font-size: 25px;
    line-height: 1;
    color: var(--cream);
    white-space: nowrap;
  }
  .info {
    font-family: "Nunito Sans", sans-serif;
    color: var(--ink);
    position: absolute;
    white-space: nowrap;
  }
  .best-before {
    left: 723px;
    top: 223px;
    font-size: 21px;
  }
  .weight {
    position: absolute;
    left: 755px;
    top: 325px;
    width: 300px;
    text-align: center;
    font-family: "Nunito Sans", sans-serif;
    font-size: 21px;
    color: var(--gold);
  }
  .credits {
    left: 590px;
    top: 413px;
    width: 500px;
    text-align: center;
    font-size: 20px;
    line-height: 25.5px;
  }
  .credits p { margin: 0; }
  .credits p + p { margin-top: 9px; }
  .size-note {
    position: absolute;
    right: 83px;
    top: 561px;
    font-family: "Marcellus", serif;
    font-size: 20px;
    color: var(--note);
  }
</style>
</head>
<body>
<div class="canvas">
  <div class="label">
    <div class="label__field"></div>
    <div class="botanical" role="img" aria-label="Acacia flower botanical pattern: yellow blossoms and green fern-like leaves"></div>
  </div>

  <svg class="art" viewBox="0 0 1200 664" aria-hidden="true">
    <!-- presentation hexagon -->
    <polygon points="484,228 553,125 553,130 490,228 543,326 661,326 708,254 663,332 540,332" fill="var(--gold-light)"/>
    <polygon points="490,228 553,130 560,130 560,326 543,326" fill="var(--gold)"/>
    <!-- title hexagon -->
    <polygon points="171,310 252,172 408,172 489,310 408,448 252,448" fill="var(--plum-soft)"/>
    <polygon points="181,310 258,182 402,182 479,310 402,439 258,439" fill="var(--plum)"/>
    <!-- banner -->
    <polygon points="176,401 189,380 470,380 482,401 470,422 189,422" fill="var(--plum-soft)"/>
    <polygon points="182,401 193,385 466,385 476,401 466,417 193,417" fill="var(--plum)"/>
    <!-- handwriting fields -->
    <polygon points="755,283 767,255 1043,255 1055,283 1043,311 767,311" fill="var(--gold-light)"/>
    <polygon points="755,346 767,318 1043,318 1055,346 1043,374 767,374" fill="var(--gold-light)"/>
    <!-- farm presentation -->
    <text transform="translate(515,247) rotate(-32)" font-family="Nunito Sans, sans-serif" font-size="19" fill="var(--ink)">
      <tspan x="0" y="0">space to put some</tspan>
      <tspan x="-3" y="27">presentation</tspan>
      <tspan x="-1" y="49">of the farm or some phrases</tspan>
    </text>
  </svg>

  <div class="brand"><span class="brand__dot"></span>PODERE TIGLIO</div>
  <div class="variety">Acacia</div>
  <div class="subtitle">Miele italiano di Acacia</div>

  <div class="info best-before">Da consumarsi preferibilmente entro</div>
  <div class="weight">weight</div>

  <div class="info credits">
    <p>Prodotto da Azienda Agricola<br>...(produced by Farm Name and address....)</p>
    <p>Confezionato presso Apicoltura<br>... (packaged at apiculture Name and address..)</p>
  </div>

  <div class="size-note">12cm X 5.5cm</div>
</div>
</body>
</html>
```